Alcohol brand needs design for gift tin packaging

We need a new design for the gift tins for our vodka brand. The bottles are in the shape of an oil barrel and the tins are also in the same shape. We would like to see the use of our logo. The gift tin needs to have a premium look.
Images of our bottles, logo and the gift tin are attached.

```html
<!DOCTYPE html>
<html lang="en">
<head>
<meta charset="utf-8">
<title>Iron Keg Vodka – Gift Tin</title>
<link rel="stylesheet" href="https://fonts.googleapis.com/css2?family=Rye&family=IM+Fell+English+SC&family=Oswald:wght@400&display=swap">
<style>
  :root {
    --bg: #f4f4f4;
    --tin-light: #c9c9c9;
    --tin-mid: #a9a9a9;
    --tin-dark: #8e8e8e;
    --ink: #2b2b2b;
    --rust: #8a4a2a;
    --band: #3a3a3a;
  }
  * { margin: 0; padding: 0; box-sizing: border-box; }
  html, body { width: 1200px; height: 900px; overflow: hidden; background: var(--bg); }
  .canvas { position: relative; width: 1200px; height: 900px; }
  .tin-label {
    position: absolute; left: 280px; top: 20px; width: 640px; height: 860px;
    background: linear-gradient(90deg, var(--tin-mid) 0%, var(--tin-light) 22%, var(--tin-dark) 45%, var(--tin-light) 70%, var(--tin-mid) 100%);
    color: var(--ink);
  }
  .band { position: absolute; left: 0; width: 100%; height: 12px; background: var(--band); }
  .band--top { top: 0; }
  .band--bottom { bottom: 0; }
  .frames { position: absolute; inset: 0; }
  .ornament, .skull { position: absolute; border-radius: 6px; }
  .ornament { width: 90px; height: 26px; left: 275px; background: rgba(43,43,43,.55); }
  .ornament--top { top: 58px; }
  .ornament--bottom { top: 778px; }
  .skull { width: 92px; height: 76px; top: 128px; background: rgba(43,43,43,.35); border-radius: 40px 40px 24px 24px; }
  .skull--left { left: 62px; }
  .skull--right { right: 62px; }
  .logo {
    position: absolute; top: 270px; left: 0; width: 100%;
    display: flex; justify-content: center; align-items: center; gap: 14px;
  }
  .logo__dot { width: 34px; height: 34px; border-radius: 50%; background: var(--rust); }
  .logo__name { font-family: "IM Fell English SC", serif; font-size: 44px; color: var(--rust); letter-spacing: 2px; }
  .title {
    position: absolute; top: 430px; width: 100%; text-align: center;
    font-family: "Rye", serif; font-size: 54px; line-height: 70px; letter-spacing: 2px; font-weight: 400;
  }
  .tagline {
    position: absolute; top: 600px; width: 100%; text-align: center;
    font-family: "IM Fell English SC", serif; font-size: 30px; letter-spacing: 1px;
  }
  .facts { position: absolute; top: 690px; left: 40px; right: 40px; display: flex; justify-content: space-between; align-items: baseline; }
  .facts__volume, .facts__abv { font-family: "Rye", serif; font-size: 34px; }
  .facts__since { font-family: "IM Fell English SC", serif; font-size: 16px; }
</style>
</head>
<body>
<main class="canvas">
  <section class="tin-label">
    <div class="band band--top"></div>
    <svg class="frames" width="640" height="860" viewBox="0 0 640 860" fill="none" stroke="#2b2b2b" stroke-width="2">
      <path d="M30 230 V90 H240"/><path d="M38 222 V98 H232"/>
      <path d="M610 230 V90 H400"/><path d="M602 222 V98 H408"/>
      <path d="M30 650 V790 H240"/><path d="M38 658 V782 H232"/>
      <path d="M610 650 V790 H400"/><path d="M602 658 V782 H408"/>
    </svg>
    <div class="ornament ornament--top" role="img" aria-label="Ornamental flourish"></div>
    <div class="skull skull--left" role="img" aria-label="Skull illustration"></div>
    <div class="skull skull--right" role="img" aria-label="Skull illustration"></div>
    <div class="logo">
      <span class="logo__dot"></span>
      <span class="logo__name">Iron Keg</span>
    </div>
    <h1 class="title">IRON KEG<br>VODKA</h1>
    <p class="tagline">DRINK CAUTIOUSLY</p>
    <div class="facts">
      <span class="facts__volume">700ML</span>
      <span class="facts__since">SINCE 2017</span>
      <span class="facts__abv">40%</span>
    </div>
    <div class="ornament ornament--bottom" role="img" aria-label="Ornamental flourish"></div>
    <div class="band band--bottom"></div>
  </section>
</main>
</body>
</html>
```